Business Card for a Mortgage Agent (myself)

I need a business card for my new job as Mortgage Agent. The Broker's logo is to be on the card as well as the brokerage License number. Not sure if to include a photo or not. Info to be on card.
Dante Roux
Mortgage Agent
Lic # M47105386
Cell: 905-614-2753
Email: danterouxk.ma@fennmail.com
Web: www.karlvostermortgages.com
TPW Brokerage Lic. # 73918

```html
<!DOCTYPE html>
<html lang="en">
<head>
<meta charset="utf-8">
<title>Dante Roux – Mortgage Agent Business Card</title>
<link rel="stylesheet" href="https://fonts.googleapis.com/css2?family=EB+Garamond:ital,wght@0,500;0,700;1,700&display=swap">
<style>
  :root {
    --backdrop: #efe9df;
    --paper: #ffffff;
    --agent-blue: #1753a1;
    --brand-blue: #0d3ea8;
    --brand-yellow: #f7c814;
    --ink-navy: #1c3d80;
    --ink-white: #ffffff;
    --card-shadow: 0 6px 18px rgba(60, 45, 25, 0.18);
  }
  * { box-sizing: border-box; margin: 0; padding: 0; }
  html, body {
    width: 840px;
    height: 1200px;
    overflow: hidden;
    background: var(--backdrop);
    font-family: "EB Garamond", Georgia, serif;
  }
  .canvas {
    position: relative;
    width: 840px;
    height: 1200px;
  }
  .card {
    position: absolute;
    left: 170px;
    width: 500px;
    height: 290px;
    background: var(--paper);
    box-shadow: var(--card-shadow);
    overflow: hidden;
  }
  .card--front { top: 290px; }
  .card--back  { top: 720px; }
  .card__art {
    position: absolute;
    inset: 0;
    width: 100%;
    height: 100%;
  }

  /* Brand lockup (name set as text, with one plain square) */
  .brand {
    position: absolute;
    display: flex;
    align-items: center;
    gap: 8px;
    color: var(--ink-navy);
    font-weight: 700;
    white-space: nowrap;
  }
  .brand__square {
    width: 16px;
    height: 16px;
    background: var(--brand-yellow);
    flex: none;
  }
  .brand__name { font-size: 17px; letter-spacing: 0.3px; }

  .card--front .brand { left: 36px; top: 138px; }

  .license-line {
    position: absolute;
    color: var(--ink-navy);
    font-weight: 700;
    font-style: italic;
    font-size: 11px;
    white-space: nowrap;
  }
  .card--front .license-line { left: 70px; bottom: 10px; }

  /* Agent identity */
  .agent {
    position: absolute;
    right: 22px;
    top: 18px;
    text-align: right;
  }
  .agent__name {
    color: var(--ink-white);
    font-weight: 700;
    font-size: 32px;
    line-height: 1;
  }
  .agent__title {
    color: var(--brand-yellow);
    font-weight: 700;
    font-size: 9.5px;
    margin-top: 2px;
  }

  /* Contact list */
  .contacts {
    position: absolute;
    left: 268px;
    top: 118px;
    list-style: none;
  }
  .contacts__item {
    display: flex;
    align-items: center;
    height: 31px;
  }
  .contacts__icon {
    width: 20px;
    height: 20px;
    flex: none;
    stroke: var(--ink-navy);
    fill: none;
    stroke-width: 1.4;
  }
  .contacts__text {
    margin-left: 30px;
    color: var(--ink-white);
    font-weight: 700;
    font-size: 10.5px;
    white-space: nowrap;
  }
  .contacts__text--web { color: var(--brand-yellow); }

  /* Back face */
  .back-panel {
    position: absolute;
    left: 146px;
    top: 66px;
    width: 200px;
    height: 150px;
    background: var(--paper);
    transform: rotate(-2deg);
  }
  .back-panel .brand {
    left: 0;
    right: 0;
    top: 52px;
    justify-content: center;
  }
  .back-panel .brand__name { font-size: 14px; }
  .back-panel .license-line {
    left: 0;
    right: 0;
    top: 108px;
    text-align: center;
    font-size: 10.5px;
  }
</style>
</head>
<body>
<main class="canvas">

  <section class="card card--front" aria-label="Business card front">
    <svg class="card__art" viewBox="0 0 500 290" aria-hidden="true">
      <rect x="250" y="0" width="250" height="290" fill="var(--brand-yellow)"/>
      <path d="M264 0 H500 V290 H304 V120 Q304 104 288 100 Q264 96 264 84 Z" fill="var(--agent-blue)"/>
      <path d="M304 150 h6 v8 h-6 z M304 182 h6 v8 h-6 z M304 212 h6 v8 h-6 z" fill="var(--agent-blue)"/>
    </svg>

    <div class="brand">
      <span class="brand__square"></span>
      <span class="brand__name">Tri Point West Mortgage</span>
    </div>
    <p class="license-line">TPW Brokerage License # 73918</p>

    <header class="agent">
      <h1 class="agent__name">Dante Roux</h1>
      <p class="agent__title">Mortgage Agent</p>
    </header>

    <ul class="contacts">
      <li class="contacts__item">
        <svg class="contacts__icon" viewBox="0 0 20 20" aria-hidden="true">
          <rect x="4" y="2" width="11" height="15" rx="1"/>
          <path d="M7 6h5M7 9h5M7 12h3"/>
          <circle cx="13" cy="15" r="2.2"/>
        </svg>
        <span class="contacts__text">Lic # M47105386</span>
      </li>
      <li class="contacts__item">
        <svg class="contacts__icon" viewBox="0 0 20 20" aria-hidden="true">
          <circle cx="10" cy="10" r="8"/>
          <path d="M7 6.5c-.8.8-.5 2.8 1.5 4.8s4 2.3 4.8 1.5l-1.4-1.4-1.2.6-2.2-2.2.6-1.2z"/>
        </svg>
        <span class="contacts__text">905-614-2753</span>
      </li>
      <li class="contacts__item">
        <svg class="contacts__icon" viewBox="0 0 20 20" aria-hidden="true">
          <rect x="3" y="5" width="14" height="10"/>
          <path d="M3 5l7 6 7-6"/>
        </svg>
        <span class="contacts__text">danterouxk.ma@fennmail.com</span>
      </li>
      <li class="contacts__item">
        <svg class="contacts__icon" viewBox="0 0 20 20" aria-hidden="true">
          <circle cx="10" cy="10" r="7.5"/>
          <ellipse cx="10" cy="10" rx="3.2" ry="7.5"/>
          <path d="M2.5 10h15M4 6h12M4 14h12"/>
        </svg>
        <span class="contacts__text contacts__text--web">www.karlvostermortgages.com</span>
      </li>
    </ul>
  </section>

  <section class="card card--back" aria-label="Business card back">
    <svg class="card__art" viewBox="0 0 500 290" aria-hidden="true">
      <rect width="500" height="290" fill="var(--brand-blue)"/>
      <polygon points="0,0 282,0 210,290 0,290" fill="var(--brand-yellow)"/>
      <polygon points="343,0 500,0 500,34" fill="var(--paper)"/>
      <polygon points="0,236 0,290 190,290" fill="var(--paper)"/>
    </svg>

    <div class="back-panel">
      <div class="brand">
        <span class="brand__square"></span>
        <span class="brand__name">Tri Point West Mortgage</span>
      </div>
      <p class="license-line">TPW Brokerage License # 73918</p>
    </div>
  </section>

</main>
</body>
</html>
```